Design a Banner for our 10 year anniversary

It's our bicycle tour company's 10th anniversary and I would like to put a new banner on our landing page to celebrate.
Check out the current banners on landing page at http://www.spokevantage.com
I need the the following items mentioned, but in no particular order.

"Celebrate our 10 year anniversary"
"2004 - 2014"

Style: Where possible, I really like the style and elements from this bicycle shirt that we designed (but never made) a few years ago.
I especially like the back and would like the banner to integrate some of these elements, or at least the "feel" where possible.
The shirt has a bit of a Hollow Lantern feel to it, (the rock band), so you may consider going for that direction or feel.
In that case, consider integrating the this Hollow Lantern lyric into the banner:
"It's been a long strange trip."

Finally, although images are not necessary, feel free to take from our Snapvelt page:
http://www.snapvelt.com/photos/spokevantage/sets/

```html
<!DOCTYPE html>
<html lang="en">
<head>
<meta charset="utf-8">
<title>Celebrating 10 Years – Anniversary Banner</title>
<link rel="stylesheet" href="https://fonts.googleapis.com/css2?family=Oswald:wght@500;700&display=swap">
<style>
  :root {
    --page-bg: #e9e6e1;
    --banner-red: #d7192a;
    --banner-red-veil: rgba(205, 24, 38, 0.58);
    --headline-white: #ffffff;
    --card-edge: #ffffff;
    --shadow: rgba(0, 0, 0, 0.35);
  }
  * { box-sizing: border-box; margin: 0; padding: 0; }
  html, body {
    width: 1200px; height: 675px; overflow: hidden;
    background: var(--page-bg);
    font-family: "Oswald", "Arial Narrow", sans-serif;
  }
  .anniversary-banner {
    position: absolute; left: 30px; top: 67px;
    width: 1140px; height: 540px;
    border: 8px solid var(--card-edge);
    box-shadow: 0 6px 18px var(--shadow);
    overflow: hidden;
  }
  .photo-collage {
    position: absolute; inset: 0;
    display: grid;
    grid-template-columns: repeat(10, 1fr);
    grid-template-rows: repeat(5, 1fr);
    gap: 3px;
    background: #f4f4f4;
  }
  .photo-tile {
    grid-column: var(--c); grid-row: var(--r);
    background: linear-gradient(160deg, var(--t1), var(--t2));
  }
  .red-veil-column {
    position: absolute; left: 190px; top: 0;
    width: 170px; height: 100%;
    background: var(--banner-red-veil);
  }
  .date-band {
    position: absolute; left: 330px; top: 38px;
    width: 320px; height: 30px;
    background: var(--banner-red);
    color: var(--headline-white);
    font-weight: 500; font-size: 19px; letter-spacing: 3px; line-height: 1;
    display: flex; align-items: center; justify-content: center;
  }
  .flag-badge {
    position: absolute; right: 40px; top: 50px;
    width: 62px; height: 42px;
    background: var(--banner-red);
    border: 3px solid var(--headline-white);
  }
  .celebrating-tag {
    position: absolute; left: 172px; top: 146px;
    padding: 4px 16px;
    background: var(--banner-red);
    color: var(--headline-white);
    font-weight: 700; font-size: 28px; line-height: 1.2; letter-spacing: 1px;
    text-transform: uppercase;
  }
  .headline-years {
    position: absolute; left: 200px; top: 190px;
    color: var(--headline-white);
    font-weight: 700; font-size: 178px; line-height: 1;
    letter-spacing: 2px;
    text-shadow: 3px 4px 8px var(--shadow);
    text-transform: uppercase;
    white-space: nowrap;
  }
  .history-strip {
    position: absolute; left: 352px; top: 384px;
    width: 470px; height: 40px;
    background: var(--banner-red);
    color: var(--headline-white);
    font-weight: 500; font-size: 26px; line-height: 1; letter-spacing: 1px;
    text-transform: uppercase;
    display: flex; align-items: center; justify-content: center;
  }
  .pennant {
    position: absolute; left: 818px; top: 350px;
  }
</style>
</head>
<body>
  <section class="anniversary-banner" aria-label="10 year anniversary banner">
    <div class="photo-collage">
      <div class="photo-tile" style="--c:1/3;--r:1/2;--t1:#2f5a33;--t2:#6e9a55" role="img" aria-label="Riders on a forest road"></div>
      <div class="photo-tile" style="--c:3/5;--r:1/2;--t1:#b23a3a;--t2:#d9c4b4" role="img" aria-label="Group of cyclists in red jerseys"></div>
      <div class="photo-tile" style="--c:5/7;--r:1/2;--t1:#7ea2c8;--t2:#5b7e58" role="img" aria-label="Cyclists under a blue sky"></div>
      <div class="photo-tile" style="--c:7/9;--r:1/2;--t1:#8fb0cf;--t2:#4f8440" role="img" aria-label="Green valley road"></div>
      <div class="photo-tile" style="--c:9/11;--r:1/3;--t1:#9ec0dc;--t2:#5e9a3e" role="img" aria-label="Alpine meadow with riders"></div>
      <div class="photo-tile" style="--c:1/2;--r:2/4;--t1:#a04848;--t2:#4d6a8a" role="img" aria-label="Rider at a celebration"></div>
      <div class="photo-tile" style="--c:2/4;--r:2/4;--t1:#8fb3d6;--t2:#4f5d4c" role="img" aria-label="Long road through the hills"></div>
      <div class="photo-tile" style="--c:4/6;--r:2/3;--t1:#8ca0b5;--t2:#7b8d6a" role="img" aria-label="Mountain pass"></div>
      <div class="photo-tile" style="--c:6/9;--r:2/4;--t1:#6d8d6a;--t2:#3f5e44" role="img" aria-label="Riders crossing a river bridge"></div>
      <div class="photo-tile" style="--c:4/6;--r:3/5;--t1:#7a7e78;--t2:#3e4a3c" role="img" aria-label="Cyclists on a descent"></div>
      <div class="photo-tile" style="--c:9/11;--r:3/5;--t1:#6fa44e;--t2:#3f6f33" role="img" aria-label="Green hills road"></div>
      <div class="photo-tile" style="--c:1/2;--r:4/6;--t1:#4a79b0;--t2:#c23a3a" role="img" aria-label="Cyclist cheering"></div>
      <div class="photo-tile" style="--c:2/4;--r:4/6;--t1:#6b9b4c;--t2:#2f4f33" role="img" aria-label="Group by the roadside"></div>
      <div class="photo-tile" style="--c:6/8;--r:4/6;--t1:#c9934e;--t2:#7a5a3a" role="img" aria-label="Harvested field"></div>
      <div class="photo-tile" style="--c:8/9;--r:4/6;--t1:#e6c52e;--t2:#8a8a70" role="img" aria-label="Yellow cycle route sign"></div>
      <div class="photo-tile" style="--c:4/6;--r:5/6;--t1:#5a87a6;--t2:#6c7d66" role="img" aria-label="Lakeside ride"></div>
      <div class="photo-tile" style="--c:9/11;--r:5/6;--t1:#7c9a64;--t2:#55704a" role="img" aria-label="Countryside path"></div>
    </div>

    <div class="red-veil-column"></div>
    <p class="date-band">2004 – 2014</p>
    <div class="flag-badge"></div>

    <p class="celebrating-tag">Celebrating</p>
    <h1 class="headline-years">10 Years</h1>
    <p class="history-strip">Of making our own history</p>
    <svg class="pennant" width="70" height="50" viewBox="0 0 70 50" aria-hidden="true">
      <polygon points="0,0 70,0 52,20 70,40 0,40" fill="var(--banner-red)"/>
    </svg>
  </section>
</body>
</html>
```